Nice concept website for free living

A website for promoting 2 concepts.

---
Live for free in amsterdam -

homeowner? --- or --- searching to rent?

HOMEOWNER PAGE:

instructions on one page --- homeowners can make x amount in a legal way - and click for more information. Form or contact direct by mobile number.

SEARCHING TO RENT PAGE:

First fill out their details quick form --- Available properties --- show available properties.

Target Market(s)

1. People needing a place to live
2. Homeowners that want more revenue from their real estate

Industry/Entity Type

Tourism

Number of Pages Required

3 page

Requirements
Must have
• Simple nice design
• Homepage quick explanation - what is the concept and choice for
• 1. Homeowners
• 2. Renters
Nice to have
• fresh design

```html
<!DOCTYPE html>
<html lang="en">
<head>
<meta charset="utf-8">
<title>Polderstay – Free Living in Netherlands</title>
<link href="https://fonts.googleapis.com/css2?family=Open+Sans:wght@400;600;700&family=Lato:wght@700&display=swap" rel="stylesheet">
<style>
  :root {
    --white: #ffffff;
    --footer-bg: #333333;
    --footer-text: #d0d0d0;
    --btn-dark: #2b2b2b;
    --btn-blue: #1560b0;
    --sky: #5f6f7c;
    --roof: #4a4438;
    --foliage: #4f5a33;
    --water: #2a2620;
  }
  * { margin: 0; padding: 0; box-sizing: border-box; }
  html, body { width: 1200px; height: 791px; overflow: hidden; }
  body { position: relative; font-family: "Open Sans", sans-serif; color: var(--white); background: var(--footer-bg); }

  .hero-photo {
    position: absolute; left: 0; top: 0; width: 1200px; height: 733px;
    background:
      radial-gradient(ellipse 420px 260px at 960px 330px, rgba(40,44,50,0.55), transparent 70%),
      radial-gradient(ellipse 300px 240px at 450px 300px, rgba(130,90,60,0.45), transparent 70%),
      linear-gradient(180deg, var(--sky) 0%, #6c767b 22%, var(--roof) 45%, #6a5a3c 62%, var(--foliage) 78%, var(--water) 100%);
  }
  .hero-shade { position: absolute; inset: 0; background: rgba(0,0,0,0.12); }

  .site-header { position: absolute; left: 0; top: 0; width: 1200px; height: 140px; }
  .brand {
    position: absolute; left: 108px; top: 74px;
    font-family: "Open Sans", sans-serif; font-size: 26px; font-weight: 600;
    color: var(--white); line-height: 34px;
  }
  .icon-btn {
    position: absolute; top: 73px; width: 45px; height: 45px;
    border: 1.5px solid var(--white); border-radius: 3px;
    display: flex; align-items: center; justify-content: center;
  }
  .icon-btn.search { left: 988px; }
  .icon-btn.menu { left: 1057px; }

  .hero-content { position: absolute; left: 0; top: 300px; width: 1200px; text-align: center; }
  .headline {
    font-family: "Open Sans", sans-serif; font-weight: 700; font-size: 43px;
    line-height: 74px; letter-spacing: 0.3px; text-transform: uppercase;
    text-shadow: 0 2px 6px rgba(0,0,0,0.6);
  }
  .choices {
    position: absolute; top: 105px; left: 385px;
    display: flex; align-items: center;
    font-family: "Lato", sans-serif; font-weight: 700; font-size: 16.5px;
  }
  .choice {
    height: 59px; display: flex; align-items: center; justify-content: center;
    color: var(--white); text-decoration: none; text-transform: uppercase;
    border-radius: 2px; box-shadow: 0 2px 6px rgba(0,0,0,0.35);
  }
  .choice.owner { width: 170px; background: var(--btn-dark); }
  .choice.renter { width: 208px; background: var(--btn-blue); }
  .choice-or { width: 51px; text-align: center; text-transform: uppercase; text-shadow: 0 1px 3px rgba(0,0,0,0.6); }

  .site-footer {
    position: absolute; left: 0; top: 733px; width: 1200px; height: 58px;
    background: var(--footer-bg); color: var(--footer-text); font-size: 12.5px;
  }
  .copyright { position: absolute; left: 99px; top: 20px; }
  .social { position: absolute; left: 913px; top: 21px; display: flex; align-items: center; font-size: 11px; color: var(--white); }
  .social-label { margin-right: 6px; }
  .social-link { width: 13px; height: 13px; background: var(--white); border-radius: 2px; margin-right: 12px; }
</style>
</head>
<body>
  <div class="hero-photo" role="img" aria-label="Dutch village scene with church tower, dark wooden houses and autumn gardens along a canal"><div class="hero-shade"></div></div>

  <header class="site-header">
    <div class="brand">Polderstay</div>
    <a class="icon-btn search" aria-label="Search">
      <svg width="26" height="26" viewBox="0 0 26 26"><circle cx="11" cy="11" r="7.5" fill="none" stroke="#fff" stroke-width="3.2"/><line x1="16.5" y1="16.5" x2="23" y2="23" stroke="#fff" stroke-width="3.8" stroke-linecap="round"/></svg>
    </a>
    <a class="icon-btn menu" aria-label="Menu">
      <svg width="26" height="22" viewBox="0 0 26 22"><g stroke="#fff" stroke-width="3.4" stroke-linecap="round"><line x1="2" y1="3" x2="24" y2="3"/><line x1="2" y1="11" x2="24" y2="11"/><line x1="2" y1="19" x2="24" y2="19"/></g></svg>
    </a>
  </header>

  <main class="hero-content">
    <h1 class="headline">Free Living in Netherlands</h1>
    <div class="choices">
      <a class="choice owner" href="#">Homeowner?</a>
      <span class="choice-or">Or</span>
      <a class="choice renter" href="#">Searching to rent?</a>
    </div>
  </main>

  <footer class="site-footer">
    <p class="copyright">Copyright © 2016,&nbsp; Polderstay. | All Rights Reserved.</p>
    <div class="social">
      <span class="social-label">Social Media :</span>
      <span class="social-link"></span>
      <span class="social-link"></span>
      <span class="social-link"></span>
      <span class="social-link"></span>
      <span class="social-link"></span>
    </div>
  </footer>
</body>
</html>
```